Front Yard Sign for Real Estate Company

Bright Door Homes is a brand new real estate broker. We need signs to put in front yard of houses that we are selling. 3D would be great. I have included the company LOGO

Target Market(s)

Residential Property buyers and sellers

Industry/Entity Type

Real Estate

Colors
ec1f27
ffc214
fbed22
ffffff

Requirements
Must have
• 3D look would be great. Logo must be included in the yard signs.
• Must include phone # to call: 555-214-6073

```html
<!DOCTYPE html>
<html lang="en">
<head>
<meta charset="UTF-8">
<title>Bright Door Homes – Yard Sign</title>
<link href="https://fonts.googleapis.com/css2?family=Montserrat:wght@700&display=swap" rel="stylesheet">
<style>
  :root {
    --backdrop: #e6e6e6;
    --paper: #ffffff;
    --gold: #efb20b;
    --gold-light: #f4c95c;
    --red: #dc2a27;
    --brand-red: #e5202a;
    --ink: #221e1f;
  }
  * { box-sizing: border-box; margin: 0; padding: 0; }
  html, body { width: 943px; height: 1200px; overflow: hidden; background: var(--backdrop); }
  body { position: relative; font-family: "Montserrat", sans-serif; }

  .sign {
    position: absolute; left: 86px; top: 86px; width: 771px; height: 1027px;
    background: var(--paper);
    box-shadow: 0 2px 10px rgba(0,0,0,0.18);
    overflow: hidden;
  }
  .sign__art { position: absolute; inset: 0; width: 100%; height: 100%; }

  .brand {
    position: absolute; left: 0; right: 0; top: 200px;
    text-align: center;
    font-weight: 700; font-size: 46px; letter-spacing: -0.5px;
    color: var(--brand-red);
  }

  .headline {
    position: absolute; left: 0; right: 0;
    text-align: center;
    font-weight: 700; font-size: 158px; line-height: 1;
    color: var(--ink); letter-spacing: 4px;
  }
  .headline--for { top: 508px; }
  .headline--sale { top: 654px; letter-spacing: 6px; }

  .call {
    position: absolute; left: 101px; top: 855px; width: 569px; height: 73px;
    background: var(--red);
    border: 1.5px solid #fff; border-radius: 5px;
    display: flex; align-items: center; justify-content: center;
    color: #fff; font-weight: 700; font-size: 44px; letter-spacing: 0.5px;
  }
</style>
</head>
<body>
  <div class="sign">
    <svg class="sign__art" viewBox="0 0 1349 1797" preserveAspectRatio="none" aria-hidden="true">
      <polygon points="0,840 674,680 1349,840 1349,1797 0,1797" fill="var(--gold)"/>
      <polygon points="35,807 674,613 1313,807 674,682" fill="var(--red)"/>
      <rect x="252" y="668" width="76" height="80" fill="var(--red)"/>
      <g fill="var(--gold-light)">
        <rect x="515" y="998" width="147" height="146"/>
        <rect x="688" y="998" width="147" height="146"/>
        <rect x="515" y="1162" width="147" height="146"/>
        <rect x="688" y="1162" width="147" height="146"/>
      </g>
    </svg>

    <div class="brand">Bright Door Homes</div>

    <div class="headline headline--for">FOR</div>
    <div class="headline headline--sale">SALE</div>

    <div class="call">Call: 555-214-6073</div>
  </div>
</body>
</html>
```